OLU58 biz card & Stationery

LU58 is a personalized shopping experience brought to you, that lets you find and discover fashion goods through a collection of boutiques curated by taste-makers - celebrities, stylists, designers, and fashion bloggers. Boutiques uses visual technology to help fashionistas discover and shop their look and creates the opportunity for designers to showcase their collections and latest inspirations online.

OLU58 is built on technology developed by our team of fashion experts who work with engineers to “teach” our computer systems to understand various patterns, pairings, and genre definitions. When signed into your account, OLU58 learns about your style and preferences and in turn, provides you better results and recommendations over time. Ultimately, OLU58 will provide shoppers with a much richer and interactive shopping experience and help drive traffic to retailers' websites.

We need a definitely cool business card. The card must be black! And must use our official logo which can be download from OLU58.com

The address for Letter head and evenlop, please use 4872 Crestwick Parkway, Sutie 510 Los Angeles CA90412, email will be anyone@OLU58.com, website is www.OLU58.com

thanks

We received some of the design, thanks. But most of the design are not what we want. We need a very clean version with black ground, you may also use some dark gray to add the element. please take a look at http://morvalstudio.no/work/#pelter__ostrama/, we do like this kind of design very much. hope it help.

```html
<!DOCTYPE html>
<html lang="en">
<head>
<meta charset="utf-8">
<title>OLU58 Business Card &amp; Stationery</title>
<link rel="stylesheet" href="https://fonts.googleapis.com/css2?family=Tenor+Sans&display=swap">
<style>
  :root {
    --page: #ffffff;
    --ink: #000000;
    --card: #0a0a0a;
    --grey: #a6a6a6;
    --grey-light: #c8c8c8;
    --grey-text: #6f6f6f;
    --shadow: rgba(0, 0, 0, 0.35);
  }
  * { margin: 0; padding: 0; box-sizing: border-box; }
  html, body { width: 1200px; height: 907px; overflow: hidden; background: var(--page); }
  .canvas { position: relative; width: 1200px; height: 907px; font-family: "Tenor Sans", sans-serif; }
  .sheet { position: absolute; background: var(--page); box-shadow: 6px 8px 14px var(--shadow); overflow: hidden; }
  .address { position: absolute; font-size: 5.5px; line-height: 8px; color: var(--grey-text); white-space: nowrap; }
  .address span { display: inline-block; width: 8px; }

  .brand { position: absolute; display: flex; align-items: center; gap: 10px; }
  .brand-square { width: 14px; height: 14px; flex: none; }
  .brand-name { font-family: "Tenor Sans", sans-serif; font-weight: 400; line-height: 1; white-space: nowrap; letter-spacing: 2px; }

  /* business card */
  .business-card { left: 116px; top: 73px; width: 234px; height: 132px; background: var(--card); }
  .business-card .address { left: 9px; top: 6px; color: #d0d0d0; }
  .business-card .brand { left: 20px; top: 46px; }
  .business-card .brand-square { background: var(--grey); }
  .business-card .brand-name { font-size: 32px; color: var(--grey-light); }
  .contact { position: absolute; right: 10px; top: 98px; text-align: right; color: #e5e5e5; font-size: 6px; line-height: 8px; padding-right: 5px; border-right: 1px solid #e5e5e5; }
  .contact .name { font-size: 7px; }
  .contact .role, .contact .email { color: #bdbdbd; }

  /* envelope */
  .envelope { left: 28px; top: 243px; width: 593px; height: 272px; }
  .envelope .address { left: 9px; top: 9px; }
  .envelope .brand { left: 14px; top: 44px; }
  .envelope .brand-square { background: var(--ink); }
  .envelope .brand-name { font-size: 36px; color: var(--grey); }

  /* letterhead */
  .letterhead { left: 634px; top: 25px; width: 542px; height: 852px; }
  .letterhead .address { left: 44px; top: 12px; }
  .letterhead .brand { left: 44px; top: 46px; }
  .letterhead .brand-square { background: var(--ink); }
  .letterhead .brand-name { font-size: 36px; color: var(--ink); }
</style>
</head>
<body>
<main class="canvas">

  <section class="sheet business-card" aria-label="Business card">
    <p class="address"><span>A</span>| 4872 Crestwick Parkway, Sutie 510 Los Angeles CA90412<br><span>W</span>| www.OLU58.com</p>
    <div class="brand">
      <div class="brand-square"></div>
      <p class="brand-name">OLU58</p>
    </div>
    <div class="contact">
      <p class="name">NAME</p>
      <p class="role">director</p>
      <p class="email">anyone@OLU58.com</p>
    </div>
  </section>

  <section class="sheet envelope" aria-label="Envelope">
    <p class="address"><span>A</span>| 4872 Crestwick Parkway, Sutie 510 Los Angeles CA90412<br><span>W</span>| www.OLU58.com</p>
    <div class="brand">
      <div class="brand-square"></div>
      <p class="brand-name">OLU58</p>
    </div>
  </section>

  <section class="sheet letterhead" aria-label="Letterhead">
    <p class="address"><span>A</span>| 4872 Crestwick Parkway, Sutie 510 Los Angeles CA90412<br><span>W</span>| www.OLU58.com</p>
    <div class="brand">
      <div class="brand-square"></div>
      <p class="brand-name">OLU58</p>
    </div>
  </section>

</main>
</body>
</html>
```